Consultative Employee Benifits Firm Needs Business Card Design Project

We need a business card design for a new company based in Northern Virginia called "Telman Financial Services, LLC. We are both a wealth management advisory firm, as well as an employee benefits firm, which strives to provide superior creativity in employee benefits plan design and greater client and employee satisfaction. We are obsessed with service and follow up.

Our firm specializes in the areas of group health, life, dental, disability, voluntary benefits, Executive Benefits, HRA and HSA programs. We offer competitive employee benefit packages and pricing models for single or multi-state/multi location companies by maintaining preferred relationships with a large number of regional and national carriers.

Our firm also considers the many dimensions of your wealth through an integrated process we call wealth structuring — a comprehensive, dynamic approach to building, preserving, enjoying and transferring your wealth. And because we are often dealing with complex ownership structures and complicated, changing family dynamics, we bring the highest level of experience and creativity to managing your wealth. We work hard to help ensure that your legacy lasts by preparing your children for the financial challenges and opportunities that are headed their way.

Our final design should communicate an integrated approach to finanial safety and optimization
Updates

 Due to a few designers not accepting due to low budget, I have increased budget payout 19%. 

Project Deadline Extended
Reason: I have only heard from 12 designers. So, maybe I did not give the right amount of time to do the project. For the designers that have submitted their designs, thank you. I have seen three or four designs that I liked and might end up with one of them after it's all over, but I thought I would see between 20 - 25 before everything was over. Dan

Target Market(s)

Professionals; doctors, contractors, small to mid size business owners, ages 50 -65 with nert worth of 2MM

Industry/Entity Type

Financial

Requirements
Must have
• Telman Financial Services, LLC

Dan Telman
President
41957 Marwick Hollow Street
Quenford Glen, 20871

Office: 703 555-0184
Cell: 703 555-0127
Fax: 703 555-0163
Email: dantelman@quorvex.net
Should not have
• No pink or yellow colors.
No generic clipart (coins, dollar signs, money bags, graphs)

```html
<!DOCTYPE html>
<html lang="en">
<head>
<meta charset="utf-8">
<title>Telman Financial Services, LLC — Business Card</title>
<link rel="stylesheet" href="https://fonts.googleapis.com/css2?family=EB+Garamond:wght@400;500&display=swap">
<style>
  :root {
    --page: #ffffff;
    --card: #000000;
    --ink: #ffffff;
  }
  * { box-sizing: border-box; margin: 0; padding: 0; }
  html, body {
    width: 1067px;
    height: 1200px;
    overflow: hidden;
    background: var(--page);
  }
  body {
    position: relative;
    font-family: "EB Garamond", "Garamond", serif;
    color: var(--ink);
  }
  .card {
    position: absolute;
    width: 934px;
    height: 534px;
    background: var(--card);
  }
  .card--front { left: 65px; top: 49px; }
  .card--back  { left: 72px; top: 610px; }

  /* Front */
  .front__name {
    position: absolute;
    left: 0; right: 0;
    top: 255px;
    text-align: center;
    font-size: 80px;
    line-height: 1;
  }
  .front__name span {
    display: inline-block;
    padding-bottom: 2px;
    border-bottom: 3px dotted var(--ink);
  }
  .front__role {
    position: absolute;
    left: 0; right: 0;
    top: 380px;
    text-align: center;
    font-size: 43px;
    line-height: 57px;
  }

  /* Back */
  .back__divider {
    position: absolute;
    left: 480px;
    top: 57px;
    width: 4px;
    height: 408px;
    background: var(--ink);
  }
  .back__identity {
    position: absolute;
    right: 499px;
    top: 150px;
    text-align: right;
    font-size: 28px;
    line-height: 38.6px;
  }
  .back__name {
    font-size: 35px;
    line-height: 44px;
  }
  .back__contact {
    position: absolute;
    left: 522px;
    top: 188px;
    font-size: 28px;
    line-height: 38.8px;
    white-space: nowrap;
  }
</style>
</head>
<body>
  <section class="card card--front">
    <h1 class="front__name"><span>Dan Telman</span></h1>
    <p class="front__role">President<br>Telman Financial Services, LLC</p>
  </section>

  <section class="card card--back">
    <div class="back__identity">
      <div class="back__name">Dan Telman</div>
      <div>President</div>
      <div>Telman Financial Services, LLC</div>
      <div>41957 Marwick Hollow Street</div>
      <div>Quenford Glen</div>
      <div>20871</div>
    </div>
    <div class="back__divider"></div>
    <div class="back__contact">
      <div>Office: 703 555-0184</div>
      <div>Cell: 703 555-0127</div>
      <div>Fax: 703 555-0163</div>
      <div>Email: dantelman@quorvex.net</div>
    </div>
  </section>
</body>
</html>
```